New Flyer Design Project

I would like to purchase a customized version of a design you have previously submitted - https://www.brivomart.example/design/58204731

I want this to be something that looks really good.
We use this to explain our service agreements.
our website is www.plorvex.example I want to stick with those colors.

```html
<!DOCTYPE html>
<html lang="en">
<head>
<meta charset="utf-8">
<title>PLX Service Plans</title>
<link rel="stylesheet" href="https://fonts.googleapis.com/css2?family=Bebas+Neue&family=Oswald:wght@500;600&family=Poppins:wght@400;500;600;700&display=swap">
<style>
  :root{
    --red:#a8282b;
    --red-dark:#8e1f22;
    --ink:#221e1f;
    --grey:#6e6e72;
    --grey-mid:#7b7b80;
    --band:#e9e9eb;
    --text:#2b2b2e;
    --white:#ffffff;
  }
  *{box-sizing:border-box;margin:0;padding:0}
  html,body{width:1200px;height:936px;overflow:hidden;background:var(--white)}
  body{position:relative;font-family:"Poppins",sans-serif;color:var(--text)}

  .header{position:absolute;left:0;top:0;width:1200px;height:170px}
  .header-bg{position:absolute;inset:0}
  .brand{position:absolute;left:62px;top:58px;display:flex;align-items:center;gap:12px}
  .brand-name{font-family:"Poppins",sans-serif;font-weight:600;font-size:48px;letter-spacing:2px;color:var(--grey-mid);line-height:1}
  .brand-dot{width:20px;height:20px;border-radius:50%;background:var(--red)}
  .title{position:absolute;left:422px;top:36px;font-family:"Bebas Neue",sans-serif;font-weight:400;font-size:112px;line-height:1;color:var(--white);letter-spacing:0.5px;white-space:nowrap}
  .title .accent{color:var(--red)}

  .band{position:absolute;left:0;top:196px;width:1200px;height:97px;background:var(--band)}
  .band-shapes{position:absolute;left:0;top:196px}
  .services-label{position:absolute;left:67px;top:220px;font-weight:700;font-size:39px;color:var(--white);letter-spacing:1px;line-height:50px}

  .plan-tabs{position:absolute;left:0;top:0}
  .plan-name{position:absolute;top:235px;font-family:"Oswald",sans-serif;font-weight:600;font-size:21px;line-height:24px;color:var(--white);white-space:nowrap;letter-spacing:-0.2px}
  .plan-price{position:absolute;top:224px;font-family:"Oswald",sans-serif;font-weight:600;font-size:21px;line-height:24px;color:var(--white);white-space:nowrap}
  .plan-price sup{font-size:11px;vertical-align:top;position:relative;top:-1px;margin-right:1px}

  .rows{position:absolute;left:0;top:319px;width:1200px;list-style:none}
  .row{display:grid;grid-template-columns:618px 278px 304px;height:26.8px;align-items:center}
  .service{display:flex;align-items:center;gap:10px;padding-left:60px;font-weight:500;font-size:16.2px;white-space:nowrap}
  .cell{display:flex;justify-content:center;align-items:center;font-weight:500;font-size:16px}
  .cell.plus{padding-left:16px}
  .cell.essentials{padding-right:18px}
  .tick{width:14px;height:14px;display:block}
  .service .tick{width:13px;height:13px}

  .divider{position:absolute;top:308px;width:1px;height:546px;background:var(--ink)}
  .divider.one{left:618px}
  .divider.two{left:896px}
  .pricing-note{position:absolute;left:618px;width:278px;top:818px;text-align:center;font-size:13.5px;color:var(--text)}

  .footer{position:absolute;left:0;top:854px;width:1200px;height:82px;background:var(--grey);display:flex;align-items:center;justify-content:center;gap:26px;color:var(--white);font-size:20px}
  .footer .item{display:flex;align-items:center;gap:10px}
  .footer svg{width:20px;height:20px}
  .footer .phone{font-weight:600}
  .notch{position:absolute;top:843px;left:0}
</style>
</head>
<body>
<svg width="0" height="0" style="position:absolute">
  <defs>
    <symbol id="tick" viewBox="0 0 20 20">
      <circle cx="10" cy="10" r="10" fill="currentColor"/>
      <path d="M5.5 10.3l3 3 6-6.4" fill="none" stroke="#fff" stroke-width="2.4" stroke-linecap="round" stroke-linejoin="round"/>
    </symbol>
    <linearGradient id="roomTone" x1="0" y1="0" x2="1" y2="0">
      <stop offset="0" stop-color="#1f1b1c"/>
      <stop offset="0.55" stop-color="#3a3637"/>
      <stop offset="1" stop-color="#1f1b1c"/>
    </linearGradient>
  </defs>
</svg>

<header class="header">
  <svg class="header-bg" width="1200" height="170" viewBox="0 0 1200 170">
    <polygon points="316,0 1200,0 1200,170 384,170" fill="url(#roomTone)" role="img" aria-label="Dim photograph of a server room aisle"/>
    <polygon points="280,0 316,0 384,170 355,170" fill="var(--red)"/>
  </svg>
  <div class="brand">
    <span class="brand-name">PLX</span>
    <span class="brand-dot"></span>
  </div>
  <h1 class="title"><span class="accent">PLX</span> SERVICE PLANS</h1>
</header>

<div class="band"></div>
<svg class="band-shapes" width="600" height="97" viewBox="0 0 600 97">
  <polygon points="0,0 235,0 230,14 0,14" fill="var(--red)"/>
  <polygon points="242,0 333,0 340,14 236,14" fill="var(--grey-mid)"/>
  <polygon points="0,14 338,14 378,84 0,84" fill="var(--ink)"/>
  <polygon points="5,84 100,84 95,97 0,97" fill="var(--grey-mid)"/>
  <polygon points="108,84 370,84 377,97 104,97" fill="var(--red)"/>
</svg>
<div class="services-label">SERVICES</div>

<svg class="plan-tabs" width="1200" height="300" viewBox="0 0 1200 300">
  <!-- small tabs above the bar -->
  <polygon points="643,227 647,219 681,219 685,227" fill="var(--grey)"/>
  <polygon points="900,227 904,219 938,219 942,227" fill="var(--grey)"/>
  <!-- main bar -->
  <polygon points="604,227 897,227 907,266 624,266" fill="var(--red)"/>
  <polygon points="897,227 1150,227 1168,266 907,266" fill="var(--grey)"/>
  <!-- price tabs -->
  <path d="M793 221q0-3 3-3h80q3 0 4 3l4 40q-40 6-84 2z" fill="var(--grey)"/>
  <path d="M1063 221q0-3 3-3h80q3 0 4 3l4 40q-40 6-84 2z" fill="var(--red)"/>
  <!-- shield icon -->
  <path d="M641 237l10-4 10 4v7c0 6-5 10-10 12c-5-2-10-6-10-12z" fill="#fff"/>
  <path d="M651 240v9M646.5 244.5h9" stroke="var(--red)" stroke-width="2" stroke-linecap="round"/>
  <!-- gear icon -->
  <g transform="translate(923,247)" fill="none" stroke="#fff" stroke-width="2.2">
    <circle r="5.5"/>
    <path d="M0 -11v4M0 7v4M-11 0h4M7 0h4M-7.8 -7.8l2.8 2.8M5 5l2.8 2.8M-7.8 7.8l2.8-2.8M5 -5l2.8-2.8"/>
  </g>
</svg>
<div class="plan-name" style="left:667px">Security Plus</div>
<div class="plan-price" style="left:807px"><sup>$</sup>75.00</div>
<div class="plan-name" style="left:941px">IT Essentials</div>
<div class="plan-price" style="left:1077px"><sup>$</sup>55.00</div>

<div class="divider one"></div>
<div class="divider two"></div>

<ul class="rows">
  <li class="row"><span class="service"><svg class="tick" style="color:var(--grey)"><use href="#tick"/></svg>Unlimited US bases Remote Help Desk Support</span><span class="cell plus"><svg class="tick" style="color:var(--red)"><use href="#tick"/></svg></span><span class="cell essentials"><svg class="tick" style="color:var(--ink)"><use href="#tick"/></svg></span></li>
  <li class="row"><span class="service"><svg class="tick" style="color:var(--grey)"><use href="#tick"/></svg>Unlimited On-Site Support</span><span class="cell plus"><svg class="tick" style="color:var(--red)"><use href="#tick"/></svg></span><span class="cell essentials">Available</span></li>
  <li class="row"><span class="service"><svg class="tick" style="color:var(--grey)"><use href="#tick"/></svg>Advanced Cybersecurity and Threat Hunting</span><span class="cell plus"><svg class="tick" style="color:var(--red)"><use href="#tick"/></svg></span><span class="cell essentials">Available</span></li>
  <li class="row"><span class="service"><svg class="tick" style="color:var(--grey)"><use href="#tick"/></svg>Managed Antivirus Protection</span><span class="cell plus"><svg class="tick" style="color:var(--red)"><use href="#tick"/></svg></span><span class="cell essentials"><svg class="tick" style="color:var(--ink)"><use href="#tick"/></svg></span></li>
  <li class="row"><span class="service"><svg class="tick" style="color:var(--grey)"><use href="#tick"/></svg>Multifactor Authentication Powered by Authora</span><span class="cell plus"><svg class="tick" style="color:var(--red)"><use href="#tick"/></svg></span><span class="cell essentials">Available</span></li>
  <li class="row"><span class="service"><svg class="tick" style="color:var(--grey)"><use href="#tick"/></svg>Cyber Security Awareness Training</span><span class="cell plus"><svg class="tick" style="color:var(--red)"><use href="#tick"/></svg></span><span class="cell essentials">Available</span></li>
  <li class="row"><span class="service"><svg class="tick" style="color:var(--grey)"><use href="#tick"/></svg>Enhanced Span Filtering</span><span class="cell plus"><svg class="tick" style="color:var(--red)"><use href="#tick"/></svg></span><span class="cell essentials">Available</span></li>
  <li class="row"><span class="service"><svg class="tick" style="color:var(--grey)"><use href="#tick"/></svg>Internet Content Filtering</span><span class="cell plus"><svg class="tick" style="color:var(--red)"><use href="#tick"/></svg></span><span class="cell essentials">Available</span></li>
  <li class="row"><span class="service"><svg class="tick" style="color:var(--grey)"><use href="#tick"/></svg>Proactive Security and System Monitoring</span><span class="cell plus"><svg class="tick" style="color:var(--red)"><use href="#tick"/></svg></span><span class="cell essentials"><svg class="tick" style="color:var(--ink)"><use href="#tick"/></svg></span></li>
  <li class="row"><span class="service"><svg class="tick" style="color:var(--grey)"><use href="#tick"/></svg>Security and Vulnerability patching</span><span class="cell plus"><svg class="tick" style="color:var(--red)"><use href="#tick"/></svg></span><span class="cell essentials"><svg class="tick" style="color:var(--ink)"><use href="#tick"/></svg></span></li>
  <li class="row"><span class="service"><svg class="tick" style="color:var(--grey)"><use href="#tick"/></svg>Backup and disaster recovery</span><span class="cell plus"><svg class="tick" style="color:var(--red)"><use href="#tick"/></svg></span><span class="cell essentials"><svg class="tick" style="color:var(--ink)"><use href="#tick"/></svg></span></li>
  <li class="row"><span class="service"><svg class="tick" style="color:var(--grey)"><use href="#tick"/></svg>Network Management and Administration</span><span class="cell plus"><svg class="tick" style="color:var(--red)"><use href="#tick"/></svg></span><span class="cell essentials"><svg class="tick" style="color:var(--ink)"><use href="#tick"/></svg></span></li>
  <li class="row"><span class="service"><svg class="tick" style="color:var(--grey)"><use href="#tick"/></svg>Novasoft Workline 365 Administration and Configuration</span><span class="cell plus"><svg class="tick" style="color:var(--red)"><use href="#tick"/></svg></span><span class="cell essentials"><svg class="tick" style="color:var(--ink)"><use href="#tick"/></svg></span></li>
  <li class="row"><span class="service"><svg class="tick" style="color:var(--grey)"><use href="#tick"/></svg>Novasoft Skyforge Administration and Configuration</span><span class="cell plus"><svg class="tick" style="color:var(--red)"><use href="#tick"/></svg></span><span class="cell essentials"><svg class="tick" style="color:var(--ink)"><use href="#tick"/></svg></span></li>
  <li class="row"><span class="service"><svg class="tick" style="color:var(--grey)"><use href="#tick"/></svg>Novasoft Panes and Server Support</span><span class="cell plus"><svg class="tick" style="color:var(--red)"><use href="#tick"/></svg></span><span class="cell essentials"><svg class="tick" style="color:var(--ink)"><use href="#tick"/></svg></span></li>
  <li class="row"><span class="service"><svg class="tick" style="color:var(--grey)"><use href="#tick"/></svg>Managed DNS</span><span class="cell plus"><svg class="tick" style="color:var(--red)"><use href="#tick"/></svg></span><span class="cell essentials"><svg class="tick" style="color:var(--ink)"><use href="#tick"/></svg></span></li>
  <li class="row"><span class="service"><svg class="tick" style="color:var(--grey)"><use href="#tick"/></svg>Hardware and Software Procurement</span><span class="cell plus"><svg class="tick" style="color:var(--red)"><use href="#tick"/></svg></span><span class="cell essentials"><svg class="tick" style="color:var(--ink)"><use href="#tick"/></svg></span></li>
  <li class="row"><span class="service"><svg class="tick" style="color:var(--grey)"><use href="#tick"/></svg>Assett Management</span><span class="cell plus"><svg class="tick" style="color:var(--red)"><use href="#tick"/></svg></span><span class="cell essentials"><svg class="tick" style="color:var(--ink)"><use href="#tick"/></svg></span></li>
</ul>

<p class="pricing-note">All Pricing is Per PC Per Month</p>

<svg class="notch" width="1200" height="12" viewBox="0 843 1200 12">
  <polygon points="607,854 618,843 629,854" fill="var(--ink)"/>
  <polygon points="885,854 896,843 907,854" fill="var(--ink)"/>
</svg>

<footer class="footer">
  <span class="item">For more Info Call Us
    <svg viewBox="0 0 20 20"><circle cx="10" cy="10" r="10" fill="#fff"/><path d="M6.5 5.5l2 -.5 1.2 2.6-1.3 1c.6 1.4 1.6 2.4 3 3l1-1.3 2.6 1.2-.5 2c-4.5.3-8.3-3.5-8-8z" fill="var(--grey)"/></svg>
    <span class="phone">(555) 013-2740</span></span>
  <span class="item">
    <svg viewBox="0 0 20 20"><circle cx="10" cy="10" r="10" fill="#fff"/><g fill="none" stroke="var(--grey)" stroke-width="1.3"><circle cx="10" cy="10" r="5.5"/><ellipse cx="10" cy="10" rx="2.4" ry="5.5"/><path d="M4.5 10h11"/></g></svg>
    www.plorvex.example</span>
  <span class="item">
    <svg viewBox="0 0 20 20"><circle cx="10" cy="10" r="10" fill="#fff"/><g fill="none" stroke="var(--grey)" stroke-width="1.3"><rect x="5" y="6.5" width="10" height="7" rx="1"/><path d="M5 7l5 4 5-4"/></g></svg>
    hello@plorvex.example</span>
</footer>
</body>
</html>
```